Business Card Design Project

Use our current logo. Clean design.

Industry/Entity Type

Business

Requirements
Must have
• Marisela DUBRANCQ
M. Law
Managing Partner

Alpenvorsa AG
Kornhalmweg 214
CH-3097 Liebefeld

M. +41 79 412 56 27
T. +41 31 928 44 10
F. +41 31 928 44 19

m.dubrancq@alpenvorsa-example.com
www.alpenvorsa-example.com

```html
<!DOCTYPE html>
<html lang="en">
<head>
<meta charset="utf-8">
<title>Alpenvorsa AG – Business Card</title>
<link rel="stylesheet" href="https://fonts.googleapis.com/css2?family=Oswald:wght@400;600&family=Source+Sans+3:wght@400;600&display=swap">
<style>
  :root {
    --bg: #c3d0db;
    --paper: #f4f4f2;
    --sun: #f2bd1d;
    --ink: #1c1a17;
    --muted: #6c6a66;
  }
  * { margin: 0; padding: 0; box-sizing: border-box; }
  html, body { width: 1200px; height: 840px; overflow: hidden; }
  body {
    background: var(--bg);
    display: flex;
    align-items: center;
    justify-content: center;
    gap: 40px;
    font-family: "Source Sans 3", Arial, sans-serif;
    color: var(--ink);
  }
  .card {
    width: 520px;
    height: 300px;
    position: relative;
    box-shadow: 0 10px 28px rgba(40, 55, 70, 0.18);
    overflow: hidden;
  }

  /* Back side: contact details */
  .card-back { background: var(--paper); }
  .card-back .brand {
    position: absolute;
    left: 40px;
    top: 66px;
    width: 170px;
    text-align: center;
    font-family: "Oswald", Arial, sans-serif;
    font-weight: 400;
    font-size: 18px;
    letter-spacing: 2px;
    color: var(--ink);
  }
  .card-back .band {
    position: absolute;
    left: 0;
    top: 146px;
    width: 232px;
    height: 22px;
    background: var(--sun);
  }
  .card-back .divider {
    position: absolute;
    left: 244px;
    top: 40px;
    width: 2px;
    height: 220px;
    background: var(--sun);
  }
  .contact {
    position: absolute;
    left: 268px;
    top: 44px;
    right: 20px;
  }
  .contact .name {
    font-family: "Oswald", Arial, sans-serif;
    font-weight: 600;
    font-size: 19px;
    letter-spacing: 0.5px;
    line-height: 1.1;
  }
  .contact .role {
    font-size: 11px;
    color: var(--sun);
    font-weight: 600;
    line-height: 1.35;
    margin-bottom: 12px;
  }
  .contact .block {
    font-size: 10.5px;
    line-height: 1.42;
    color: var(--muted);
    margin-bottom: 8px;
  }
  .contact .block b { color: var(--ink); font-weight: 600; }
  .contact dl {
    display: grid;
    grid-template-columns: 20px auto;
    font-size: 10.5px;
    line-height: 1.42;
    color: var(--muted);
    margin-bottom: 8px;
  }
  .contact dt { color: var(--ink); }

  /* Front side: brand */
  .card-front {
    background: var(--sun);
    display: flex;
    flex-direction: column;
    align-items: center;
    justify-content: center;
    gap: 14px;
  }
  .card-front .brand {
    font-family: "Oswald", Arial, sans-serif;
    font-weight: 400;
    font-size: 48px;
    letter-spacing: 6px;
    color: var(--ink);
  }
  .card-front .rule {
    width: 230px;
    height: 2px;
    background: var(--ink);
  }
</style>
</head>
<body>
  <section class="card card-back" aria-label="Business card back">
    <div class="brand">ALPENVORSA</div>
    <div class="band"></div>
    <div class="divider"></div>
    <div class="contact">
      <p class="name">Marisela DUBRANCQ</p>
      <p class="role">M. Law · Managing Partner</p>
      <p class="block"><b>Alpenvorsa AG</b><br>Kornhalmweg 214<br>CH-3097 Liebefeld</p>
      <dl>
        <dt>M.</dt><dd>+41 79 412 56 27</dd>
        <dt>T.</dt><dd>+41 31 928 44 10</dd>
        <dt>F.</dt><dd>+41 31 928 44 19</dd>
      </dl>
      <p class="block">m.dubrancq@alpenvorsa-example.com<br>www.alpenvorsa-example.com</p>
    </div>
  </section>

  <section class="card card-front" aria-label="Business card front">
    <div class="brand">ALPENVORSA</div>
    <div class="rule"></div>
  </section>
</body>
</html>
```